Flyer Design Project

Need a creative flyer design for a new coffee shop. The name of the coffee shop is Plum Kettle. We sell coffees, teas, espresso based drinks, pastries and freshly made mini donuts.
Looking for the flyer to have the following:
1. Now Open
2. advertisement: try our freshly made mini donuts 6 for $1
3. advertisement: 1/2 price coffee Monday's
4. address: 938 north 6th street, Brookvale, PA 17215
5. pictures of coffee and lattes
6. the logo
7. offers end June 30, 2013
8. Free Wifi
Feel free to be creative. I want the flyer to be eye catching. Open to different sizes and shapes to the flyer.
Note: flyer can be one or two sided. I do not have any additional photos.
Industry/Entity Type
Coffee Shop
Look and feel
Each slider illustrates characteristics of the customer's brand and the style your logo design should communicate.

```html
<!DOCTYPE html>
<html lang="en">
<head>
<meta charset="utf-8">
<title>Plum Kettle – Now Open</title>
<link rel="stylesheet" href="https://fonts.googleapis.com/css2?family=Aldrich&family=Alfa+Slab+One&family=Archivo+Black&family=Francois+One&family=Open+Sans:wght@400&display=swap">
<style>
  :root {
    --orange: #f7860f;
    --orange-deep: #d8650a;
    --dark: #3a2412;
    --bg-dark: #2e1b0d;
    --bg-mid: #6a4018;
    --cream: #f4c48a;
  }
  html, body {
    margin: 0;
    padding: 0;
    width: 1200px;
    height: 1200px;
    overflow: hidden;
    background: var(--bg-dark);
  }
  .flyer {
    display: block;
    width: 1200px;
    height: 1200px;
  }
  .big-letter {
    font-family: "Archivo Black", sans-serif;
    stroke: var(--orange);
    stroke-width: 7;
    paint-order: stroke;
  }
  .intro {
    font-family: "Aldrich", sans-serif;
    fill: var(--orange);
    font-size: 62px;
  }
  .outlined-dark {
    fill: var(--dark);
    stroke: var(--orange);
    stroke-width: 5;
    paint-order: stroke;
  }
  .outlined-orange {
    fill: var(--orange);
    stroke: var(--dark);
    stroke-width: 6;
    paint-order: stroke;
  }
  .condensed { font-family: "Francois One", sans-serif; }
  .slab { font-family: "Alfa Slab One", serif; }
  .wifi {
    font-family: "Aldrich", sans-serif;
    fill: var(--orange);
    font-size: 80px;
  }
  .address {
    font-family: "Aldrich", sans-serif;
    fill: var(--cream);
    font-size: 30px;
  }
  .brand-name {
    font-family: "Francois One", sans-serif;
    fill: var(--orange);
    font-size: 62px;
  }
  .offer-end {
    font-family: "Open Sans", sans-serif;
    fill: var(--orange);
    font-size: 22px;
  }
</style>
</head>
<body>
<svg class="flyer" viewBox="0 0 1238 1238" xmlns="http://www.w3.org/2000/svg">
  <defs>
    <radialGradient id="bg-glow" cx="50%" cy="52%" r="60%">
      <stop offset="0" stop-color="#a7621f"/>
      <stop offset="0.45" stop-color="#6a4018"/>
      <stop offset="1" stop-color="#2e1b0d"/>
    </radialGradient>
    <linearGradient id="fill-cup-beans" x1="0" y1="0" x2="0" y2="1">
      <stop offset="0" stop-color="#c9661e"/>
      <stop offset="0.35" stop-color="#eee9de"/>
      <stop offset="0.6" stop-color="#8a4a1c"/>
      <stop offset="1" stop-color="#5a2a10"/>
    </linearGradient>
    <radialGradient id="fill-donut" cx="50%" cy="50%" r="55%">
      <stop offset="0" stop-color="#f08a5a"/>
      <stop offset="1" stop-color="#d35a2c"/>
    </radialGradient>
    <linearGradient id="fill-coffee-cup" x1="0" y1="0" x2="0" y2="1">
      <stop offset="0" stop-color="#2a1a10"/>
      <stop offset="0.45" stop-color="#cfd9c8"/>
      <stop offset="1" stop-color="#6e4a2a"/>
    </linearGradient>
    <linearGradient id="fill-grinder" x1="0" y1="0" x2="1" y2="1">
      <stop offset="0" stop-color="#e07a20"/>
      <stop offset="0.5" stop-color="#b83e0c"/>
      <stop offset="1" stop-color="#5a200a"/>
    </linearGradient>
    <linearGradient id="fill-latte" x1="0" y1="0" x2="1" y2="1">
      <stop offset="0" stop-color="#c45a14"/>
      <stop offset="0.45" stop-color="#e8e4dc"/>
      <stop offset="1" stop-color="#a0602a"/>
    </linearGradient>
    <linearGradient id="fill-beans" x1="0" y1="0" x2="0" y2="1">
      <stop offset="0" stop-color="#8c3a14"/>
      <stop offset="0.5" stop-color="#c0561e"/>
      <stop offset="1" stop-color="#6a2a0e"/>
    </linearGradient>
    <radialGradient id="badge-glow" cx="50%" cy="45%" r="55%">
      <stop offset="0" stop-color="#fff4e6"/>
      <stop offset="0.55" stop-color="#8a6a4a"/>
      <stop offset="1" stop-color="#2a180a"/>
    </radialGradient>
  </defs>

  <rect class="background" width="1238" height="1238" fill="url(#bg-glow)"/>

  <g class="headline-now-open">
    <text class="big-letter" role="img" aria-label="Letter N filled with a photo of a coffee cup on beans" x="148" y="388" font-size="380" textLength="244" lengthAdjust="spacingAndGlyphs" fill="url(#fill-cup-beans)">N</text>
    <text class="big-letter" role="img" aria-label="Letter O shaped as a sugared donut photo" x="142" y="676" font-size="380" textLength="268" lengthAdjust="spacingAndGlyphs" fill="url(#fill-donut)">O</text>
    <text class="big-letter" role="img" aria-label="Letter P filled with a photo of a steaming espresso cup" x="412" y="672" font-size="380" textLength="226" lengthAdjust="spacingAndGlyphs" fill="url(#fill-coffee-cup)">P</text>
    <text class="big-letter" role="img" aria-label="Letter E filled with a photo of a coffee grinder" x="646" y="672" font-size="380" textLength="192" lengthAdjust="spacingAndGlyphs" fill="url(#fill-grinder)">E</text>
    <text class="big-letter" role="img" aria-label="Letter N filled with a photo of a latte cup with cinnamon" x="842" y="672" font-size="380" textLength="242" lengthAdjust="spacingAndGlyphs" fill="url(#fill-latte)">N</text>
    <text class="big-letter" role="img" aria-label="Letter W filled with a photo of roasted coffee beans" x="146" y="956" font-size="380" textLength="294" lengthAdjust="spacingAndGlyphs" fill="url(#fill-beans)">W</text>
  </g>

  <g class="offer-donuts">
    <text class="intro" x="418" y="166" textLength="650" lengthAdjust="spacing">try our freshly made</text>
    <text class="condensed outlined-dark" x="420" y="270" font-size="72" textLength="280" lengthAdjust="spacing">mini</text>
    <text class="condensed outlined-dark" x="420" y="366" font-size="124" textLength="276" lengthAdjust="spacingAndGlyphs">donuts</text>
    <text class="slab outlined-orange" x="716" y="306" font-size="140" textLength="124" lengthAdjust="spacingAndGlyphs">6</text>
    <text class="slab outlined-dark" x="710" y="370" font-size="70" textLength="132" lengthAdjust="spacingAndGlyphs">for</text>
    <text class="slab outlined-orange" x="852" y="372" font-size="200" textLength="236" lengthAdjust="spacingAndGlyphs">$1</text>
  </g>

  <g class="offer-coffee">
    <text class="slab outlined-orange" x="468" y="848" font-size="176" textLength="282" lengthAdjust="spacingAndGlyphs">1/2</text>
    <text class="slab outlined-dark" x="465" y="936" font-size="90" textLength="276" lengthAdjust="spacingAndGlyphs">price</text>
    <text class="condensed outlined-dark" x="765" y="806" font-size="144" textLength="325" lengthAdjust="spacingAndGlyphs">coffee</text>
    <text class="condensed outlined-orange" x="765" y="882" font-size="104" textLength="325" lengthAdjust="spacingAndGlyphs">mondays</text>
  </g>

  <g class="details">
    <text class="wifi" x="165" y="1098" textLength="485" lengthAdjust="spacing">FREE WIFI!</text>
    <line x1="130" y1="1122" x2="745" y2="1122" stroke="var(--orange)" stroke-width="2"/>
    <text class="address" x="168" y="1170" textLength="480" lengthAdjust="spacingAndGlyphs">938 north 6th street, Brookvale, PA 17215</text>
  </g>

  <g class="brand-badge">
    <circle cx="935" cy="1110" r="186" fill="url(#badge-glow)" stroke="var(--orange)" stroke-width="10"/>
    <text class="brand-name" x="935" y="1150" text-anchor="middle" textLength="290" lengthAdjust="spacingAndGlyphs">Plum Kettle</text>
  </g>

  <text class="offer-end" transform="translate(1202 1202) rotate(-90)">Offers end June 30, 2013</text>
</svg>
</body>
</html>
```